New modern website for Kerbline Groundworks

Hi we are an existing company that has a current website http://www.kerblinegroundworks.co.nz/ we are looking to get a new vibrant looking website designed to take us further and gain more customers. We are after a simple easy to use website that does not confuse but we want to make an impact and stand out from the rest

Target Market(s)

Homeowners And Commercial Businesses

Industry/Entity Type

It Company

Coding

Coded - Design and coding required

Number of Pages Required

2 page

```html
<!DOCTYPE html>
<html lang="en">
<head>
<meta charset="utf-8">
<title>Kerbline Groundworks – Concrete &amp; Asphalt Paving</title>
<link href="https://fonts.googleapis.com/css2?family=Figtree:wght@300;400;600;700&display=swap" rel="stylesheet">
<style>
:root{
  --ink:#1d1d1d;
  --muted:#8a8a8a;
  --red:#f4483b;
  --yellow:#fde74c;
  --soft:#f7f7f7;
  --white:#ffffff;
  --dark:#222220;
}
*{margin:0;padding:0;box-sizing:border-box}
html,body{width:797px;height:1200px;overflow:hidden;background:var(--white)}
body{position:relative;font-family:"Figtree",sans-serif;color:var(--ink)}
.abs{position:absolute}

/* header */
.site-header{left:0;top:0;width:797px;height:51px;background:var(--white)}
.brand{left:162px;top:17px;font-size:15px;font-weight:700;letter-spacing:.3px;color:var(--ink);display:flex;align-items:center;gap:6px}
.brand-dot{width:9px;height:9px;background:var(--red)}
.nav{left:418px;top:0;height:51px;display:flex;font-size:6.5px;text-transform:uppercase;color:#777}
.nav a{display:flex;align-items:center;height:51px;padding:0 6px;color:inherit;text-decoration:none}
.nav a.active{background:var(--yellow);color:var(--ink);padding:0 11px}

/* hero */
.hero{left:0;top:51px;width:797px;height:188px;background:linear-gradient(100deg,#6e7a4a 0%,#3b3a30 25%,#8a3a22 45%,#5b4a3a 60%,#3a2c22 100%)}
.hero-title{left:163px;top:112px;font-size:25px;font-weight:700;color:var(--white)}
.hero-sub{left:164px;top:143px;font-size:15px;font-weight:400;color:var(--white)}
.quote-title{left:498px;top:92px;font-size:14px;font-weight:700;color:var(--white)}
.field{left:496px;width:125px;height:20px;background:var(--white);font-size:6px;color:#999;padding:7px 8px}
.submit{left:496px;top:175px;width:125px;height:18px;background:var(--red);color:var(--white);font-size:7px;font-weight:600;display:flex;align-items:center;justify-content:center}

/* trusted */
.trusted{left:0;top:239px;width:797px;height:191px;background:var(--soft)}
.section-lead{left:162px;font-size:12px;font-weight:600;color:var(--ink)}
.feature-icon{top:290px;width:36px;height:36px}
.feature{top:339px;width:140px;height:68px;border-left:1.5px solid var(--yellow);padding-left:13px}
.feature h3{font-size:9.5px;font-weight:400;margin-top:0}
.feature p{font-size:5.6px;line-height:10px;color:#777;margin-top:9px}

/* content blocks */
.block-title{font-size:19px;font-weight:600}
.block-text{width:218px;font-size:7.2px;line-height:12.4px;color:var(--muted);font-weight:300;height:110px;overflow:hidden}
.btn{width:68px;height:21px;background:var(--red);color:var(--white);font-size:7px;display:flex;align-items:center;justify-content:center;box-shadow:0 2px 6px rgba(244,72,59,.4)}
.photo{box-shadow:0 6px 14px rgba(0,0,0,.25)}

/* gallery */
.gallery{left:0;top:866px;width:797px;height:167px;background:var(--soft)}
.thumb{top:915px;width:149px;height:101px}

/* footer */
.contact-band{left:0;top:1033px;width:797px;height:167px;background:linear-gradient(120deg,#2a2a26 0%,#3b3224 40%,#262522 70%,#1e1e1d 100%)}
.contact-line{left:0;width:797px;text-align:center;color:var(--white)}
.contact-q{font-size:18px;font-weight:700}
.rule{left:349px;top:1129px;width:100px;height:1.5px;background:var(--red)}
.contact-phone{top:1138px;font-size:15px;font-weight:400}
</style>
</head>
<body>

<header class="abs site-header">
  <div class="abs brand"><span class="brand-dot"></span>Kerbline Groundworks</div>
  <nav class="abs nav">
    <a class="active">Home</a><a>About</a><a>Services</a><a>Projects</a><a>Contact us</a>
  </nav>
</header>

<section class="abs hero" role="img" aria-label="Close-up of a road roller on a fresh asphalt site"></section>
<h1 class="abs hero-title">Concrete &amp; Asphalters</h1>
<p class="abs hero-sub">Settings the standarts for quality</p>
<h2 class="abs quote-title">Get quick quote</h2>
<div class="abs field" style="top:122px">Name</div>
<div class="abs field" style="top:146px">Phone</div>
<div class="abs submit">Submit</div>

<section class="abs trusted"></section>
<h2 class="abs section-lead" style="top:258px">The trusted name for all Concrete &amp; Asphalt Paving in Auckland</h2>

<svg class="abs feature-icon" style="left:162px" viewBox="0 0 36 36" fill="none" stroke="#f4483b" stroke-width="1.3">
  <circle cx="18" cy="18" r="13"/><circle cx="18" cy="18" r="8"/><circle cx="18" cy="18" r="4"/>
  <g stroke-width="2.2"><path d="M18 2v3M18 31v3M2 18h3M31 18h3M6.7 6.7l2 2M27.3 27.3l2 2M6.7 29.3l2-2M27.3 8.7l2-2"/></g>
</svg>
<svg class="abs feature-icon" style="left:322px;width:46px" viewBox="0 0 46 36" fill="none" stroke="#f4483b" stroke-width="1.3">
  <path d="M2 26V17h8l4-6h10v15M24 20h14v6"/><path d="M26 12l10-7 6 8-4 3"/>
  <circle cx="9" cy="27" r="4"/><circle cx="32" cy="27" r="4"/><path d="M13 27h15"/>
</svg>
<svg class="abs feature-icon" style="left:485px" viewBox="0 0 36 36" fill="none" stroke="#f4483b" stroke-width="1.3">
  <path d="M8 15a10 10 0 0 1 20 0z"/><path d="M5 15h26"/><path d="M18 5v4"/>
  <path d="M6 34v-6a6 6 0 0 1 6-6h12a6 6 0 0 1 6 6v6z"/><path d="M14 22l4 6 4-6"/>
</svg>

<div class="abs feature" style="left:163px">
  <h3>Our experience</h3>
  <p>We have a reputation with clients in and around Auckland for achieving great results on time and within budget every time. We are proud to share our years of experience.</p>
</div>
<div class="abs feature" style="left:323px">
  <h3>Concreting &amp; Asphalt</h3>
  <p>When it comes to all asphalt services, you can rest assured we will work around your schedule, requirements and budget. Servicing throughout Auckland, we specialise in.</p>
</div>
<div class="abs feature" style="left:485px">
  <h3>Additional Services</h3>
  <p>As part of our asphalt services, we are proud to offer a range of related services to our clients in the eastern suburbs and greater Auckland. Specialising in residential, commercial and industrial projects.</p>
</div>

<h2 class="abs block-title" style="left:162px;top:452px">Services</h2>
<p class="abs block-text" style="left:162px;top:488px">But I must explain to you how all this mistaken idea of denouncing pleasure and praising pain was born and I will give you a complete account of the system, and expound the actual teachings of the great explorer of the truth, the master-builder of human happiness. No one rejects, dislikes, or avoids pleasure itself, because it is pleasure, but because those who do not know how to pursue pleasure rationally encounter consequences that are extremely painful. Nor again is there anyone who loves or pursues or</p>
<div class="abs btn" style="left:162px;top:611px">Read more</div>
<div class="abs photo" style="left:405px;top:473px;width:229px;height:127px;background:linear-gradient(180deg,#8fb8dc 0%,#5f8a4a 40%,#3a3a38 70%,#2b2b2a 100%)" role="img" aria-label="Road roller compacting new asphalt beside trees"></div>

<div class="abs photo" style="left:162px;top:681px;width:230px;height:127px;background:linear-gradient(180deg,#5a7a3a 0%,#7b8a6a 35%,#8e9296 70%,#6f7478 100%)" role="img" aria-label="Finished asphalt driveway lined with garden plants"></div>
<h2 class="abs block-title" style="left:417px;top:660px">Projects</h2>
<p class="abs block-text" style="left:417px;top:696px">But I must explain to you how all this mistaken idea of denouncing pleasure and praising pain was born and I will give you a complete account of the system, and expound the actual teachings of the great explorer of the truth, the master-builder of human happiness. No one rejects, dislikes, or avoids pleasure itself, because it is pleasure, but because those who do not know how to pursue pleasure rationally encounter consequences that are extremely painful. Nor again is there anyone who loves or pursues or</p>
<div class="abs btn" style="left:417px;top:819px">Look now</div>

<section class="abs gallery"></section>
<h2 class="abs section-lead" style="top:886px">For residential driveways and commercial paving in Auckland</h2>
<div class="abs thumb" style="left:162px;background:#3a2b22" role="img" aria-label="Red chip residential driveway"></div>
<svg class="abs" style="left:223px;top:957px" width="26" height="16" viewBox="0 0 26 16" fill="none" stroke="#fff" stroke-width="1.8">
  <path d="M1 8s5-7 12-7 12 7 12 7-5 7-12 7S1 8 1 8z"/><circle cx="13" cy="8" r="3.5" fill="#fff"/>
</svg>
<div class="abs thumb" style="left:324px;background:linear-gradient(180deg,#6e8a4a 0%,#8a8d8e 25%,#6d7172 100%)" role="img" aria-label="Grey asphalt driveway with kerb edge"></div>
<div class="abs thumb" style="left:486px;background:linear-gradient(180deg,#6e8a4a 0%,#a07060 25%,#8c5d4c 100%)" role="img" aria-label="Red chip sealed driveway near a house"></div>

<section class="abs contact-band" role="img" aria-label="Dark photo of a road roller on a paving job"></section>
<p class="abs contact-line contact-q" style="top:1076px">Any Questions you would like to ask?</p>
<p class="abs contact-line contact-q" style="top:1099px">Need to talk to us...</p>
<div class="abs rule"></div>
<p class="abs contact-line contact-phone">MOBILE: 027 5180246 OR PHONE: 09 61 43 207</p>

</body>
</html>
```